Property Management company

We need a design for our company Maplecrest Elder Commons. We are complex of apartments that we manage and operate. We do like the colors green or blue

Industry/Entity Type

Property Management,

Requirements
Must have
• color
Nice to have
• maybe be able to use as a watermark

```html
<!DOCTYPE html>
<html lang="en">
<head>
<meta charset="utf-8">
<title>Maplecrest Elder Commons — Letterhead</title>
<link rel="stylesheet" href="https://fonts.googleapis.com/css2?family=Montserrat:wght@400;500;700&display=swap">
<style>
  :root {
    --backdrop: #e6e6e6;
    --paper: #ffffff;
    --ink: #2b2b2b;
    --ink-strong: #111111;
    --brand-deep: #0a2a72;
    --brand-mid: #1565c8;
    --brand-bright: #18c6f0;
    --accent-red: #e5262c;
    --icon-dark: #3a3a3a;
    --watermark: rgba(120, 170, 215, 0.16);
  }
  * { box-sizing: border-box; margin: 0; padding: 0; }
  html, body {
    width: 1200px; height: 1000px; overflow: hidden;
    background: var(--backdrop);
    font-family: "Montserrat", sans-serif;
    color: var(--ink);
  }
  .letterhead {
    position: absolute; left: 277px; top: 82px;
    width: 646px; height: 836px;
    background: var(--paper);
    overflow: hidden;
  }
  .brand {
    position: absolute; left: 0; right: 0; top: 46px;
    display: flex; flex-direction: column; align-items: center; gap: 8px;
  }
  .brand-dot {
    width: 48px; height: 48px; border-radius: 50%;
    background: linear-gradient(135deg, var(--brand-bright), var(--brand-deep));
  }
  .brand-name { font-size: 11px; font-weight: 500; color: var(--ink-strong); letter-spacing: .2px; }

  .sender { position: absolute; left: 63px; top: 159px; font-size: 10px; line-height: 16px; }
  .sender-name { font-size: 11px; font-weight: 700; color: var(--ink-strong); }
  .sender-role { font-size: 8px; line-height: 12px; margin-bottom: 2px; }
  .sender-line span { display: inline-block; width: 20px; }

  .date { position: absolute; left: 418px; top: 220px; font-size: 10px; }

  .watermark {
    position: absolute; left: 170px; top: 290px; width: 300px; height: 180px;
    background: radial-gradient(ellipse at center, var(--watermark), rgba(255,255,255,0) 70%);
  }

  .body { position: absolute; left: 63px; top: 272px; width: 520px; font-size: 10px; line-height: 20.7px; }
  .body p { margin-bottom: 20.7px; }
  .body p span { display: block; white-space: nowrap; overflow: hidden; }

  .signature-mark {
    position: absolute; left: 63px; top: 626px; width: 95px; height: 22px;
    background: linear-gradient(90deg, rgba(40,40,40,.18), rgba(40,40,40,.05));
    border-radius: 4px;
  }
  .signatory { position: absolute; left: 64px; top: 650px; font-size: 12px; line-height: 12px; color: var(--ink-strong); }

  .contacts { position: absolute; top: 700px; left: 128px; display: flex; gap: 26px; font-size: 8.5px; line-height: 12px; }
  .contact { display: flex; align-items: center; gap: 8px; }
  .contact-icon { width: 21px; height: 21px; display: flex; align-items: center; justify-content: center; }
  .contact-icon.red { background: var(--accent-red); }
  .contact-icon.dark { background: var(--icon-dark); }

  .footer-band {
    position: absolute; left: 0; bottom: 0; width: 646px; height: 105px;
    background: linear-gradient(90deg, var(--brand-bright) 0%, var(--brand-mid) 45%, #0e4fb0 65%, var(--brand-deep) 100%);
  }
</style>
</head>
<body>
<main class="letterhead">
  <header class="brand">
    <div class="brand-dot"></div>
    <div class="brand-name">Maplecrest Elder Commons</div>
  </header>

  <section class="sender">
    <div class="sender-name">Owen Hartley</div>
    <div class="sender-role">Chief Director,</div>
    <div class="sender-line"><span>A :</span>48 Birchfield Lane, Maplecrest - 2045</div>
    <div class="sender-line"><span>W :</span>office@maplecrestcommons.com, www.maplecrestcommons.com</div>
    <div class="sender-line"><span>P :</span>+000-123-456-789</div>
  </section>
  <div class="date">Date, 00 September, 0000</div>

  <div class="watermark" role="img" aria-label="Faint isometric illustration of apartment blocks as a watermark"></div>

  <section class="body">
    <p>
      <span>This is a sample letter that has been placed to demonstrate typing remat (Your Company). letterhead</span>
      <span>design. When positioned properly, it will serve to work in harmony with all other elements letterhead.</span>
      <span>This letterhead design is meant to project an image</span>
    </p>
    <p>
      <span>This letterhead design is meant project an image of professionalism reliability. By using simple aligen</span>
      <span>we have created a very spacious feeling. The simplicity suggest&nbsp; rengththe spaciousnes contributes h</span>
      <span>aesthetics the layout. These basic qualities along with the (Your Company)</span>
    </p>
    <p>
      <span>look and helps reinforce the (Your Company) brand. letterhead design is meant to project an image p</span>
      <span>design. When positioned properly, it will serve to work in harmony all the other elements letterhead.</span>
      <span>sionalism and reliability.</span>
    </p>
    <p>
      <span>This letterhead design is based on the (Form of your logo) form (Your Company) logo. Each stationery</span>
      <span>we have created a very spacious feeling. The simplicity suggests strength the spaciousnes contribute</span>
      <span>part of the (Form of your logo).</span>
    </p>
  </section>

  <div class="signature-mark" role="img" aria-label="Handwritten signature"></div>
  <div class="signatory">Clara Benton<br>Manager.</div>

  <footer class="contacts">
    <div class="contact">
      <div class="contact-icon red">
        <svg width="12" height="12" viewBox="0 0 24 24"><path fill="#fff" d="M6.6 10.8a15 15 0 0 0 6.6 6.6l2.2-2.2c.3-.3.7-.4 1-.2 1.1.4 2.3.6 3.6.6.6 0 1 .4 1 1V20c0 .6-.4 1-1 1A17 17 0 0 1 3 4c0-.6.4-1 1-1h3.5c.6 0 1 .4 1 1 0 1.3.2 2.5.6 3.6.1.3 0 .7-.2 1z"/></svg>
      </div>
      <div>+000 12345 6789<br>+000 12345 6789</div>
    </div>
    <div class="contact">
      <div class="contact-icon dark">
        <svg width="12" height="12" viewBox="0 0 24 24"><circle cx="12" cy="12" r="9" fill="none" stroke="#fff" stroke-width="2"/><path d="M3 12h18M12 3c3 3 3 15 0 18M12 3c-3 3-3 15 0 18" fill="none" stroke="#fff" stroke-width="1.6"/></svg>
      </div>
      <div>maplecrestcommons.com<br>hello@maplecrestcommons.com</div>
    </div>
    <div class="contact">
      <div class="contact-icon red">
        <svg width="11" height="13" viewBox="0 0 24 28"><path fill="#fff" d="M12 1a9 9 0 0 0-9 9c0 7 9 17 9 17s9-10 9-17a9 9 0 0 0-9-9zm0 12.5a3.5 3.5 0 1 1 0-7 3.5 3.5 0 0 1 0 7z"/></svg>
      </div>
      <div>Street Address Here<br>Maplecrest, 2045</div>
    </div>
  </footer>

  <div class="footer-band" role="img" aria-label="Isometric illustration of glowing blue buildings with people working at computers"></div>
</main>
</body>
</html>
```